Thank You Card

I'm looking for a thank you card design using our logo and other graphics. We are an essential business and our employees (Electricians) have done an incredible job staying healthy and safe during the COVID-19 pandemic, I want to send each a thank you card.

```html
<!DOCTYPE html>
<html lang="en">
<head>
<meta charset="utf-8">
<title>Thank You Card</title>
<link rel="stylesheet" href="https://fonts.googleapis.com/css2?family=Nunito+Sans:wght@300;800;900&display=swap">
<style>
  :root {
    --deep-blue: #0a5f8c;
    --mid-blue: #1d8fb8;
    --sky-blue: #7cc3dc;
    --glow: #ffffff;
    --ink: #ffffff;
    --brand-blue: #1f3a93;
  }
  html, body {
    margin: 0;
    padding: 0;
    width: 1200px;
    height: 937px;
    overflow: hidden;
    background: #ffffff;
  }
  .card {
    position: relative;
    width: 1200px;
    height: 937px;
    overflow: hidden;
    font-family: "Nunito Sans", sans-serif;
  }
  .card-photo {
    position: absolute;
    inset: 0;
    background:
      radial-gradient(ellipse 300px 360px at 285px 520px, var(--glow) 0%, rgba(255,255,255,0.95) 40%, rgba(255,255,255,0) 100%),
      linear-gradient(180deg, rgba(255,255,255,0) 38%, rgba(230,247,252,0.85) 48%, rgba(255,255,255,0) 58%),
      radial-gradient(ellipse 520px 700px at 250px 500px, #d9eef6 0%, rgba(217,238,246,0) 100%),
      linear-gradient(100deg, #cfe8f2 0%, var(--sky-blue) 35%, var(--mid-blue) 68%, var(--deep-blue) 100%);
  }
  .headline {
    position: absolute;
    left: 640px;
    top: 78px;
    margin: 0;
    color: var(--ink);
    font-weight: 300;
    line-height: 1;
  }
  .headline-lead {
    display: block;
    font-size: 68px;
    line-height: 70px;
    letter-spacing: 1px;
  }
  .headline-focus {
    display: block;
    font-size: 106px;
    line-height: 116px;
    letter-spacing: -1px;
  }
  .thanks {
    position: absolute;
    left: 638px;
    top: 790px;
    margin: 0;
    color: var(--ink);
    font-size: 78px;
    font-weight: 900;
    letter-spacing: -2px;
    line-height: 1;
  }
  .brand {
    position: absolute;
    left: 116px;
    top: 820px;
    width: 300px;
    text-align: center;
    color: var(--brand-blue);
    font-size: 32px;
    font-weight: 800;
    line-height: 1.1;
  }
</style>
</head>
<body>
  <main class="card">
    <div class="card-photo" role="img" aria-label="Photograph of a glowing clear incandescent light bulb with a horizontal streak of light across a blue background"></div>
    <h1 class="headline">
      <span class="headline-lead">Lighting life in<br>the darkness of</span>
      <span class="headline-focus">COVID 19</span>
    </h1>
    <p class="thanks">THANK YOU...</p>
    <p class="brand">Brightline<br>Service Co.</p>
  </main>
</body>
</html>
```